High Tech Real Estate Startup needs a business card

We are developing an innovative real estate marketing product based around advanced search and virtual reality.

We talk to people, we need business cards.

Target Market(s)

The target market is technology professionals and realtors.

Contact Information for Business Card

The information to be included will include

Name
Title
Phone Number
E-mail Address
www.quelzo.com

It should use simple iconography for each one of those fields.

Font styles to use
Other font styles liked:
• Co, Jubilat, Avenir

Colors

Designer to choose colors to be used in the design.

Requirements
Must have
• Clean aesthetic,
• Good use of negative space.
• It should use our company logo, shown in the attached file. It is able to use the negative of that logo (coloured font and white background) and I have attached other acceptable accent colours in a swatch file.
Should not have
• Should not be too busy
• No extraneous text (slogans, tag lines etc)

```html
<!DOCTYPE html>
<html lang="en">
<head>
<meta charset="utf-8">
<title>Quelzo Business Card</title>
<link rel="stylesheet" href="https://fonts.googleapis.com/css2?family=Barlow+Condensed:ital,wght@1,400&family=Barlow+Semi+Condensed:wght@600&family=Montserrat:wght@500&family=Nunito+Sans:wght@300&display=swap">
<style>
  :root {
    --teal: #13bcc0;
    --orange: #cc5a21;
    --stage: #3b3b3d;
    --paper: #ffffff;
    --ink: #333335;
  }
  html, body {
    margin: 0;
    padding: 0;
    overflow: hidden;
    background: var(--paper);
  }
  .canvas {
    position: relative;
    width: 1142px;
    height: 1200px;
    overflow: hidden;
    background: var(--paper);
  }
  .stage {
    position: absolute;
    left: 77px;
    top: 74px;
    width: 1065px;
    height: 1065px;
    background: var(--stage);
  }
  .card {
    position: absolute;
    left: 264px;
    width: 706px;
    height: 431px;
    background: var(--paper);
  }
  .card--front { top: 143px; }
  .card--back { top: 664px; }

  .pattern-field {
    position: absolute;
    background: linear-gradient(135deg, #16c0c4 0%, #11b6ba 50%, #15bec2 100%);
    display: flex;
    align-items: center;
    justify-content: center;
  }
  .card--front .pattern-field {
    left: 21px;
    top: 19px;
    width: 666px;
    height: 391px;
  }
  .card--back .pattern-field {
    left: 344px;
    top: 46px;
    width: 343px;
    height: 346px;
  }
  .wordmark {
    font-family: "Montserrat", sans-serif;
    font-weight: 500;
    color: var(--paper);
    letter-spacing: 2px;
    line-height: 1;
  }
  .card--front .wordmark { font-size: 78px; }
  .card--back .wordmark { font-size: 55px; }

  .holder-name {
    position: absolute;
    left: 23px;
    top: 45px;
    margin: 0;
    font-family: "Barlow Semi Condensed", sans-serif;
    font-weight: 600;
    font-size: 43px;
    line-height: 1;
    color: var(--orange);
    letter-spacing: -0.5px;
    white-space: nowrap;
  }
  .holder-title {
    position: absolute;
    left: 26px;
    top: 91px;
    width: 248px;
    height: 34px;
    margin: 0;
    background: var(--teal);
    color: var(--paper);
    font-family: "Barlow Condensed", sans-serif;
    font-style: italic;
    font-weight: 400;
    font-size: 29px;
    line-height: 34px;
    text-align: center;
  }
  .contact-list {
    position: absolute;
    left: 28px;
    top: 264px;
    margin: 0;
    padding: 0;
    list-style: none;
  }
  .contact-item {
    display: flex;
    align-items: center;
    height: 38px;
    margin-bottom: 9px;
  }
  .contact-item:last-child { margin-top: 3px; }
  .contact-icon {
    width: 38px;
    height: 38px;
    background: var(--teal);
    flex: none;
  }
  .contact-text {
    margin-left: 24px;
    font-family: "Nunito Sans", sans-serif;
    font-weight: 300;
    font-size: 28px;
    color: var(--ink);
    line-height: 1;
    position: relative;
    top: 6px;
    white-space: nowrap;
  }
</style>
</head>
<body>
<div class="canvas">
  <div class="stage"></div>

  <section class="card card--front">
    <div class="pattern-field" role="img" aria-label="Teal background with a subtle diamond pattern">
      <span class="wordmark">QUELZO</span>
    </div>
  </section>

  <section class="card card--back">
    <h1 class="holder-name">MARCO KORREN</h1>
    <p class="holder-title">Director</p>

    <ul class="contact-list">
      <li class="contact-item">
        <svg class="contact-icon" viewBox="0 0 38 38" aria-hidden="true">
          <rect width="38" height="38" fill="var(--teal)"/>
          <path d="M12 10c-2 1-3 3-2 6 2 6 6 10 12 12 3 1 5 0 6-2l-4-4-3 2c-3-1-6-4-7-7l2-3z" fill="none" stroke="#fff" stroke-width="2" stroke-linejoin="round"/>
          <path d="M21 11a7 7 0 0 1 6 6M21 15a3 3 0 0 1 2 2" fill="none" stroke="#fff" stroke-width="1.6" stroke-linecap="round"/>
        </svg>
        <span class="contact-text">416.555.0182</span>
      </li>
      <li class="contact-item">
        <svg class="contact-icon" viewBox="0 0 38 38" aria-hidden="true">
          <rect width="38" height="38" fill="var(--teal)"/>
          <rect x="9" y="13" width="20" height="13" fill="#fff"/>
          <path d="M9 13l10 8 10-8" fill="none" stroke="var(--teal)" stroke-width="1.5"/>
        </svg>
        <span class="contact-text">hello@quelzo.com</span>
      </li>
      <li class="contact-item">
        <svg class="contact-icon" viewBox="0 0 38 38" aria-hidden="true">
          <rect width="38" height="38" fill="var(--teal)"/>
          <circle cx="19" cy="19" r="10" fill="#fff"/>
          <g fill="none" stroke="var(--teal)" stroke-width="1.3">
            <ellipse cx="19" cy="19" rx="4.5" ry="10"/>
            <line x1="19" y1="9" x2="19" y2="29"/>
            <line x1="9" y1="19" x2="29" y2="19"/>
            <path d="M11 14h16M11 24h16"/>
          </g>
        </svg>
        <span class="contact-text">www.quelzo.com</span>
      </li>
    </ul>

    <div class="pattern-field" role="img" aria-label="Teal square with a subtle diamond pattern">
      <span class="wordmark">QUELZO</span>
    </div>
  </section>
</div>
</body>
</html>
```